Web Design and logo

A new company based on creative professionals.. linking their artistic resources. Art, photography, music, and writing.

Target Market(s)

Artists buyers

Industry/Entity Type

It Company

Coding

Coded - Design and coding required

Number of Pages Required

3 page

Font styles to use
Decorative

Colors

Designer to choose colors to be used in the design.

Requirements
Nice to have
• Logo design based on Lumen Artisan Guild

```html
<!DOCTYPE html>
<html lang="en">
<head>
<meta charset="utf-8">
<title>Lumen Artisan Guild</title>
<link rel="stylesheet" href="https://fonts.googleapis.com/css2?family=Lato:wght@400;700;900&family=Open+Sans:ital,wght@0,400;0,600;1,400&display=swap">
<style>
:root{
  --blue:#3b8de4;
  --blue-deep:#2a6fd8;
  --ink:#2b2b2b;
  --text:#6d6d6d;
  --muted:#9a9a9a;
  --hex-grey:#5c5c5c;
  --panel:#f0f0f0;
  --footer:#ececec;
  --white:#ffffff;
}
*{box-sizing:border-box;margin:0;padding:0}
html,body{width:1200px;height:3030px;overflow:hidden}
body{position:relative;background:var(--white);font-family:"Open Sans",Arial,sans-serif;color:var(--text)}
.abs{position:absolute}

/* header */
.site-header{position:absolute;left:0;top:0;width:1200px;height:115px;background:var(--white)}
.brand{position:absolute;left:117px;top:38px;font-family:"Lato",sans-serif;font-weight:700;font-size:28px;color:var(--ink);letter-spacing:.2px}
.main-nav{position:absolute;top:47px;left:0;width:1200px;font-family:"Open Sans",sans-serif;font-size:15px;color:var(--ink)}
.main-nav span{position:absolute;white-space:nowrap}
.main-nav .active{color:var(--blue)}
.nav-bar{position:absolute;left:456px;top:0;width:50px;height:4px;background:var(--blue)}
.search-icon{position:absolute;left:1040px;top:49px}

/* hero */
.hero{position:absolute;left:0;top:115px;width:1200px;height:572px;overflow:hidden;
  background:radial-gradient(ellipse at 12% 30%,#b3261e 0,#8e1d18 18%,transparent 38%),
             radial-gradient(ellipse at 90% 25%,#b62a22 0,#8a1b16 18%,transparent 38%),
             radial-gradient(ellipse at 66% 60%,#a2231d 0,transparent 10%),
             linear-gradient(180deg,#9a9a9a 0,#cfcfcf 40%,#8a8a8a 100%)}
.hero-title{position:absolute;left:0;top:148px;width:1200px;text-align:center;font-family:"Lato",sans-serif;font-weight:900;font-size:41px;line-height:46px;color:var(--white);text-transform:uppercase}
.hero-btn{position:absolute;left:487px;top:257px;width:214px;height:48px;border:2px solid var(--white);border-radius:24px;color:var(--white);font-family:"Lato",sans-serif;font-weight:700;font-size:15px;text-align:center;line-height:44px}
.hero-dots{position:absolute;left:560px;top:469px;display:flex;gap:8px}
.hero-dots i{width:13px;height:13px;border-radius:50%;border:2px solid var(--white)}
.hero-dots i.on{background:var(--white)}
.hero-curve{position:absolute;left:0;top:495px}

/* welcome */
.welcome-kicker{position:absolute;left:0;top:670px;width:1200px;text-align:center;font-family:"Lato",sans-serif;font-size:34px;color:var(--blue)}
.welcome-title{position:absolute;left:0;top:706px;width:1200px;text-align:center;font-family:"Lato",sans-serif;font-size:36px;color:var(--ink)}
.divider{position:absolute;left:555px;top:761px;width:90px;height:3px;background:#8c8c8c}
.welcome-copy{position:absolute;left:210px;top:780px;width:780px;text-align:center;font-size:15px;line-height:28px;color:var(--text)}
.hex{position:absolute;top:930px;width:236px;height:246px}
.hex-label{position:absolute;left:0;width:236px;text-align:center;color:var(--white);font-family:"Open Sans",sans-serif;font-size:17px;line-height:21px}

/* how creative */
.feature-art{position:absolute;left:0;top:1216px;width:610px;height:467px;
  background:radial-gradient(circle at 62% 55%,#5f8fa6 0,#b06a3a 20%,transparent 45%),
             linear-gradient(120deg,#e4e1dc 0,#c9c3b8 45%,#7d8b8c 100%)}
.feature-panel{position:absolute;left:610px;top:1216px;width:590px;height:467px;background:linear-gradient(135deg,#f5f5f5 0,#e6e6e6 100%)}
.feature-title{position:absolute;left:610px;top:1325px;width:590px;text-align:center;font-family:"Lato",sans-serif;font-size:31px;color:var(--ink)}
.feature-copy{position:absolute;left:650px;width:510px;text-align:center;font-size:13px;line-height:20px;color:var(--muted)}
.btn-outline{position:absolute;left:784px;top:1551px;width:148px;height:44px;border:2px solid var(--blue);border-radius:22px;color:var(--blue);font-size:14px;font-weight:600;text-align:center;line-height:40px}

/* work */
.work{position:absolute;left:0;top:1687px;width:1200px;height:551px;background:linear-gradient(90deg,#3a86e6 0,#5aa3f2 30%,#4b94ee 60%,#2f78de 100%)}
.work-title{position:absolute;left:0;top:1724px;width:1200px;text-align:center;font-family:"Lato",sans-serif;font-size:31px;color:var(--white)}
.tile{position:absolute;width:232px;height:190px;border:4px solid var(--white)}

/* testimonial */
.section-title{position:absolute;left:0;top:2320px;width:1200px;text-align:center;font-family:"Lato",sans-serif;font-size:31px;color:var(--ink)}
.avatar-ring{position:absolute;left:263px;top:2398px;width:152px;height:152px;border-radius:50%;border:3px solid var(--blue);background:var(--white)}
.avatar{position:absolute;left:272px;top:2407px;width:134px;height:134px;border-radius:50%;background:linear-gradient(180deg,#d9d9d9,#b9b9b9)}
.quote-mark{position:absolute;font-family:"Lato",sans-serif;font-weight:900;font-size:72px;line-height:72px;color:var(--blue)}
.quote-text{position:absolute;left:481px;top:2404px;width:470px;font-style:italic;font-size:16px;line-height:26px;color:var(--text)}
.author{position:absolute;left:484px;top:2506px;font-size:15px;line-height:28px;color:var(--ink)}

/* footer */
.site-footer{position:absolute;left:0;top:2646px;width:1200px;height:384px;background:var(--footer);border-top:2px solid #dcdcdc}
.foot-col{position:absolute;top:2700px}
.foot-col h3{font-family:"Lato",sans-serif;font-weight:400;font-size:23px;color:var(--ink);margin-bottom:12px}
.foot-col li{list-style:none;font-size:13px;line-height:25px;color:var(--ink)}
.social{position:absolute;top:2746px;left:838px;display:flex;gap:8px}
.social i{width:37px;height:37px;border-radius:50%;border:2px solid var(--ink)}
.foot-rule{position:absolute;left:115px;top:2966px;width:962px;height:1px;background:#bdbdbd}
.copyright{position:absolute;left:0;top:2986px;width:1200px;text-align:center;font-size:13px;color:var(--muted)}
</style>
</head>
<body>

<header class="site-header">
  <div class="brand">Lumen Artisan Guild</div>
  <div class="nav-bar"></div>
  <nav class="main-nav">
    <span class="active" style="left:459px">Home</span>
    <span style="left:537px">About Us</span>
    <span style="left:641px">Our Services</span>
    <span style="left:771px">Work</span>
    <span style="left:847px">Blogs</span>
    <span style="left:923px">Contact Us</span>
  </nav>
  <svg class="search-icon" width="20" height="20" viewBox="0 0 20 20" aria-hidden="true"><circle cx="8" cy="8" r="6" fill="none" stroke="#9a9a9a" stroke-width="2"/><line x1="12.5" y1="12.5" x2="18" y2="18" stroke="#9a9a9a" stroke-width="2.4"/></svg>
</header>

<section class="hero" role="img" aria-label="Painted street scene with a tower, red autumn trees and a woman holding a red umbrella">
  <h1 class="hero-title">Art &amp; Photography Creative<br>Professionals</h1>
  <div class="hero-btn">View Our Work</div>
  <div class="hero-dots"><i class="on"></i><i class="on"></i><i></i><i></i></div>
  <svg class="hero-curve" width="1200" height="80" viewBox="0 0 1200 80" preserveAspectRatio="none" aria-hidden="true"><path d="M0 80 Q600 -40 1200 80 Z" fill="#fff"/></svg>
</section>

<section class="welcome">
  <div class="welcome-kicker">Welcome to</div>
  <h2 class="welcome-title">Lumen Artisan Guild</h2>
  <div class="divider"></div>
  <p class="welcome-copy">ligula pulvinar metus eget consectetuer augue nisi quis lacus Ut ac mi quis lacus mollis aliquam Curabitur iaculis tempus eros Curabitur vel mi sit amet magna malesuada ultrices Ut nisi erat fermentum vel congue id euismod in elit Fusce ultricies orci ac feugiat</p>

  <svg class="abs" style="left:0;top:900px" width="1200" height="300" aria-hidden="true">
    <defs><filter id="hexShadow" x="-20%" y="-20%" width="140%" height="140%"><feDropShadow dx="0" dy="6" stdDeviation="7" flood-color="#000" flood-opacity=".35"/></filter></defs>
    <g filter="url(#hexShadow)">
      <polygon points="199,40 319,40 376,150 319,260 199,260 142,150" fill="#3b8de4" transform="translate(0,-4) scale(1,0.92)"/>
      <polygon points="431,40 551,40 608,150 551,260 431,260 374,150" fill="#5c5c5c" transform="translate(0,-4) scale(1,0.92)"/>
      <polygon points="669,40 789,40 846,150 789,260 669,260 612,150" fill="#3b8de4" transform="translate(0,-4) scale(1,0.92)"/>
      <polygon points="904,40 1024,40 1081,150 1024,260 904,260 847,150" fill="#5c5c5c" transform="translate(0,-4) scale(1,0.92)"/>
    </g>
    <!-- pencil cup -->
    <g fill="none" stroke="#fff" stroke-width="3" stroke-linejoin="round">
      <path d="M246 80 h26 l-3 40 h-20 z"/>
      <path d="M252 80 v-24 l3 -6 l3 6 v24"/><path d="M262 80 v-18 l3 -5 l3 5 v18"/>
    </g>
    <!-- brush -->
    <g fill="none" stroke="#fff" stroke-width="3" stroke-linecap="round">
      <line x1="512" y1="56" x2="484" y2="100"/>
      <path d="M484 100 q-10 2 -10 14 q10 0 14 -10 z" fill="#fff"/>
    </g>
    <!-- guitar -->
    <g fill="none" stroke="#fff" stroke-width="3" stroke-linecap="round">
      <ellipse cx="716" cy="112" rx="16" ry="12" transform="rotate(-35 716 112)"/>
      <line x1="726" y1="104" x2="752" y2="78"/>
      <circle cx="714" cy="113" r="3"/>
    </g>
    <!-- quill -->
    <g fill="#fff">
      <path d="M990 62 q-30 10 -34 44 l-4 8 l4 1 l4 -8 q28 -8 30 -45 z"/>
    </g>
  </svg>
  <div class="hex-label" style="left:141px;top:1036px">Artistic<br>Resources</div>
  <div class="hex-label" style="left:373px;top:1036px">Art &amp;<br>Photography</div>
  <div class="hex-label" style="left:611px;top:1050px">Music</div>
  <div class="hex-label" style="left:846px;top:1043px">Writing</div>
</section>

<section class="feature">
  <div class="feature-art" role="img" aria-label="Watercolour portrait in profile dissolving into colourful paint splashes"></div>
  <div class="feature-panel"></div>
  <h2 class="feature-title">How Creative we are</h2>
  <p class="feature-copy" style="top:1388px">Vivamus porttitor purus nisi eleifend libero a tempus libero lectus feugiat felis Morbi diam mauris viverra in gravida eu</p>
  <p class="feature-copy" style="top:1440px">libero id ullamcorper nonummy nibh ligula pulvinar metus eget consectetuer augue nisi quis lacus Ut ac mi quis lacus mollis aliquam Curabitur iaculis tempus eros Curabitur vel mi sit amet magna malesuada ultrices Ut nisi erat fermentum vel congue</p>
  <div class="btn-outline">Learn More</div>
</section>

<section class="work">
</section>
<h2 class="work-title">Our Work</h2>
<div class="tile" style="left:121px;top:1790px;background:linear-gradient(160deg,#c9a47e,#8a3a1f 60%,#d9b98f)" role="img" aria-label="Painted red poppies"></div>
<div class="tile" style="left:361px;top:1790px;background:linear-gradient(180deg,#f2f2f2,#cfcfcf)" role="img" aria-label="Sketch of a crystal chandelier"></div>
<div class="tile" style="left:601px;top:1790px;background:linear-gradient(135deg,#0d1f44,#2f6fb8 55%,#0b1530)" role="img" aria-label="Music notes on a blue glowing background"></div>
<div class="tile" style="left:841px;top:1790px;background:radial-gradient(circle at 55% 40%,#e07a2a 0,#3a3a3a 30%,#1c1c1c 100%)" role="img" aria-label="Hot air balloon in a night sky"></div>
<div class="tile" style="left:121px;top:1988px;background:linear-gradient(180deg,#7fb6d6,#4f8a5c 60%,#d8d4cc)" role="img" aria-label="Hand writing in a notebook by a lake"></div>
<div class="tile" style="left:361px;top:1988px;background:linear-gradient(180deg,#2d6f73,#12393d)" role="img" aria-label="Elephant swimming underwater"></div>
<div class="tile" style="left:601px;top:1988px;background:linear-gradient(135deg,#c9b8d6,#3a4a6a 50%,#e0c8c0)" role="img" aria-label="Abstract ink painting of a figure"></div>
<div class="tile" style="left:841px;top:1988px;background:linear-gradient(180deg,#bdbdbd,#5a5a5a 70%,#d8b22a)" role="img" aria-label="Painted city street with a yellow taxi"></div>

<section class="testimonial">
  <h2 class="section-title">What People Says</h2>
  <svg class="abs" style="left:112px;top:2448px" width="24" height="34" aria-hidden="true"><polyline points="20,3 5,17 20,31" fill="none" stroke="#8f8f8f" stroke-width="3"/></svg>
  <svg class="abs" style="left:1008px;top:2448px" width="24" height="34" aria-hidden="true"><polyline points="4,3 19,17 4,31" fill="none" stroke="#8f8f8f" stroke-width="3"/></svg>
  <div class="avatar-ring"></div>
  <div class="avatar" role="img" aria-label="Portrait photo of the reviewer"></div>
  <div class="quote-mark" style="left:418px;top:2392px">“</div>
  <p class="quote-text">Aociosqu ad litora torquent per conubia nostra per inceptos hymenaeos Proin nulla arcu nonummy luctus dictum eget fermentum et lorem Nunc porta convallis pede</p>
  <div class="quote-mark" style="left:852px;top:2462px">”</div>
  <div class="author">By Author Name<br>Vireo Program Manager</div>
</section>

<footer class="site-footer"></footer>
<div class="foot-col" style="left:117px"><h3>Company</h3><ul><li>Home</li><li>About Us</li><li>Our Services</li><li>Why Us</li></ul></div>
<div class="foot-col" style="left:327px"><h3>Services</h3><ul><li>Artistic Resources</li><li>Art</li><li>Photography</li><li>Music and writing</li></ul></div>
<div class="foot-col" style="left:604px"><h3>Resources</h3><ul><li>Blogs</li><li>Help</li><li>Terms of Use</li><li>Contact Us</li></ul></div>
<div class="foot-col" style="left:836px"><h3>Follow Us</h3></div>
<div class="social" aria-label="Social links"><i></i><i></i><i></i><i></i></div>
<div class="foot-rule"></div>
<div class="copyright">© 2017 Company Name  All right reserved</div>

</body>
</html>
```